Brelvo Pizza & Pasta Takeaway Flyer

Our takeaway shop needs a well designed flyer for print and letter box distribution. Design to have a clear list of menu, Specials, contact details. If menu doesn't fit into A4, we won't mind going upto extended A4. I have attached draft copy of our menu and list of item in excel. Please add 5mm Bleed to the flyer.
Flyer will get printed on 115gsm Gloss stock.

```html
<!DOCTYPE html>
<html lang="en">
<head>
<meta charset="utf-8">
<title>Brelvo Pizza &amp; Pasta – Takeaway Flyer</title>
<link href="https://fonts.googleapis.com/css2?family=Arimo:wght@400;700&family=Roboto+Condensed:wght@400;700&display=swap" rel="stylesheet">
<style>
:root{
  --green:#6db33f;
  --green-dark:#3f7d1f;
  --brown:#5a2a14;
  --red:#9e2f2d;
  --ink:#1e1a16;
  --grey:#333;
  --paper:#ffffff;
  --stage:#ecebe8;
}
*{box-sizing:border-box;margin:0;padding:0}
html,body{width:1200px;height:1200px;overflow:hidden;background:var(--stage)}
body{font-family:"Arimo",Arial,sans-serif;color:var(--ink)}
.flyer{position:absolute;left:0;top:282px;width:1200px;height:636px;display:flex;box-shadow:0 4px 14px rgba(0,0,0,.25)}
.panel{width:300px;height:100%;display:flex;flex-direction:column;overflow:hidden}
.item{display:flex;align-items:baseline;white-space:nowrap}
.item .dots{flex:1;border-bottom:1.5px dotted currentColor;margin:0 2px;transform:translateY(-3px);opacity:.8}
.desc{font-family:"Roboto Condensed",Arial Narrow,sans-serif;font-size:9px;line-height:1.25;text-align:justify}
.heading{text-align:center;font-weight:700;color:var(--brown);font-size:13px}

/* panel 1 */
.menu-green{background:var(--green)}
.menu-green .list{padding:6px 14px 0 14px;flex:1}
.menu-green .item{font-family:"Roboto Condensed",sans-serif;font-size:10.5px;line-height:1.23}
.menu-green .heading{margin:3px 0 1px}
.menu-green .heading:first-child{margin-top:0}
.photo{display:block}
.salad-photo{height:117px;background:radial-gradient(ellipse at 45% 60%,#4f8f2a 0,#7cbf48 45%,#a9cf8a 80%)}

/* panel 2 */
.menu-white{background:var(--paper)}
.dessert-photo{height:165px;background:radial-gradient(circle at 58% 55%,#c7a0d6 0,#d8c0e4 18%,#f0e6d8 40%,#fafafa 75%)}
.menu-white .list{padding:4px 18px 0 15px;flex:1}
.menu-white .item{font-size:12.5px;line-height:1.3}
.menu-white .heading{margin:2px 0 3px}
.menu-white .desc{margin-bottom:2px}
.dinner{background:var(--green);height:104px;padding:4px 16px 0 15px;color:#111}
.dinner .item{font-size:15.5px;font-weight:700}
.dinner .pack{font-family:"Roboto Condensed",sans-serif;font-size:9px;line-height:1.2;margin-top:1px;white-space:nowrap;overflow:hidden}
.dinner .pack b{font-family:"Arimo",sans-serif;font-size:12.5px}

/* panel 3 */
.deals-panel{background:var(--paper)}
.deals-photo{height:193px;background:radial-gradient(ellipse at 50% 60%,#e2a23a 0,#f2c36a 28%,#f5efe2 55%,#fff 80%)}
.deals{padding:0 14px 0 15px;flex:1}
.deals .heading{font-size:13px;margin-top:2px}
.deals .note{text-align:center;font-size:12px;color:var(--grey);margin:6px 0 8px}
.deal{margin-bottom:8px;color:var(--grey)}
.deal .item{font-size:15px;font-weight:700;color:var(--brown)}
.deal p{font-size:12.5px;line-height:1.25}
.terms{font-size:10px;font-style:italic;text-align:center;color:var(--grey);margin-top:-4px;line-height:1.3}
.contact{background:var(--red);color:#fff;height:104px;text-align:center;padding-top:2px}
.contact .label{font-size:10px;font-weight:700}
.contact .phone{font-size:19px;line-height:1.25}
.contact .addr{font-size:13px;line-height:1.3}
.contact .web{font-size:18px;line-height:1.35}

/* panel 4 */
.cover{background:#3a3a3a}
.brand-area{height:220px;background:linear-gradient(180deg,#2f2f2f,#4a4a48);display:flex;align-items:center;justify-content:center;gap:10px}
.brand-mark{width:22px;height:22px;border-radius:50%;background:var(--red)}
.brand-name{color:#fff;font-size:19px;font-weight:700}
.pizza-photo{flex:1;background:radial-gradient(circle at 62% 45%,#c44a24 0,#d98b3c 38%,#8a4a26 55%,#6b6058 72%,#4b4540 100%)}
.site-band{height:26px;background:var(--green);color:#2b2b2b;font-size:11px;letter-spacing:8px;text-align:center;line-height:26px}
</style>
</head>
<body>
<main class="flyer">

  <section class="panel menu-green">
    <div class="list">
      <h2 class="heading">RIBS &amp; WINGS</h2>
      <div class="item">Pork Ribs<span class="dots"></span>$17</div>
      <div class="item">Beef Ribs<span class="dots"></span>$15</div>
      <div class="item">Buffalo Wings&nbsp;&nbsp;(6 Pcs)<span class="dots"></span>$8</div>
      <div class="item">BBQ Wings&nbsp;&nbsp;(6 Pcs)<span class="dots"></span>$8</div>
      <div class="item">Honey Soy wings&nbsp;&nbsp;(6 Pcs)<span class="dots"></span>$8</div>
      <div class="item">Fried Wings&nbsp;&nbsp;(6 Pcs)<span class="dots"></span>$8</div>
      <div class="item">with Tomato Sauce</div>
      <div class="item">Chicken Lollipop&nbsp;&nbsp;(5 Pcs)<span class="dots"></span>$8</div>
      <div class="item">With Lemon Wedges</div>

      <h2 class="heading">THE AB</h2>
      <div class="item">AB Chicken<span class="dots"></span>$13.95</div>
      <p class="desc">Marinated Chicken,Cheese on Top of Fries, Drizzled with Ranch, BBQ &amp; Garlic Sauce</p>
      <div class="item">AB Meat L<span class="dots"></span>$13.95</div>
      <p class="desc">Cheese, Pulled Beef, Bacon, Ham on Top of Fries, Drizzled with Ranch, BBQ &amp; Garlic Sauce</p>
      <div class="item">AB Combin<span class="dots"></span>$13.95</div>
      <p class="desc">Cheese, Chicken, Pulled Beef, Ham on Top of Fries, Drizzled with Ranch, BBQ &amp; Garlic Sauce</p>
      <div class="item">AB Veg<span class="dots"></span>$13.95</div>
      <p class="desc">Cheese, Tomato, Capsicum, Mushroom, crumbed Fetta, Pineappleon Top of Fries, Drizzled with Ranch, Tomato &amp; Garlic Sauce</p>
      <div class="item">AB Doubl<span class="dots"></span>$11.95</div>
      <p class="desc">Double Cheese on Top of Fries, Drizzled with Ranch, Tomato &amp; Garlic Sauce</p>

      <h2 class="heading">SALAD</h2>
      <div class="item">Garden Salad<span class="dots"></span>$6</div>
      <p class="desc">Mixed Leaves, Tomato, Cucumber, Olives, Onion, Cucumber, Pineapple &amp; Italian dressing</p>
      <div class="item">Greek Salad<span class="dots"></span>$6</div>
      <p class="desc">Mixed Leaves, Tomato, Cucumber, Olives, Onion, Fetta &amp; Dressed with Lemon Juice, Olive Oil, White wine vinegar</p>
      <div class="item">Coleslaw<span class="dots"></span>$6</div>
      <p class="desc">Red Cabbages, Green Cabbage, Carrot, Onion mixed with Mayonnaise and Lemon</p>
      <div class="item">Chicken Ceaser Salad<span class="dots"></span>$9</div>
      <p class="desc">Mixed Leaves, Chicken, Crispy Bacon, Croutons, Parmesan Cheese &amp; Ceaser Dressing</p>
    </div>
    <div class="photo salad-photo" role="img" aria-label="Photo of a bowl of fresh green leaf salad"></div>
  </section>

  <section class="panel menu-white">
    <div class="photo dessert-photo" role="img" aria-label="Photo of a berry ice cream scoop with mint and a swiss roll"></div>
    <div class="list">
      <h2 class="heading">DESSERT</h2>
      <div class="item">Chocolate Sundae<span class="dots"></span>$4.95</div>
      <div class="item">Choconut Calzone<span class="dots"></span>$6</div>
      <p class="desc">Calzone filled with Choconut &amp; topped with Icing Sugar</p>
      <div class="item">Berry Zone<span class="dots"></span>$9</div>
      <p class="desc">Choconut Calzone filled with Mixed Berry &amp; topped with Icing Sugar</p>
      <div class="item">White Valcone<span class="dots"></span>$9</div>
      <p class="desc">Calzone filled with White Chocolate &amp; topped with Icing Sugar</p>
      <div class="item">Crumbo Calzone<span class="dots"></span>$9</div>
      <p class="desc">Calzone rolled with Crumbo, filled with White Chocolate &amp; topped with Icing Sugar</p>
      <div class="item">Tropical Calzone<span class="dots"></span>$9</div>
      <p class="desc">Choconut Calzone filled with Mango and Pineapple &amp; topped with Icing Sugar</p>

      <h2 class="heading">DRINKS</h2>
      <div class="item">Can<span class="dots"></span>$2.95</div>
      <p class="desc">Kola, Diet Kola, Kola Zero, Fizzo, Limey</p>
      <div class="item">1.25 lit<span class="dots"></span>$4.95</div>
      <p class="desc">Kola, Diet Kola, Kola Zero, Fizzo, Limey</p>
      <div class="item">Leafton Ice Tea<span class="dots"></span>$3.95</div>
      <div class="item">Orange Juice<span class="dots"></span>$4.50</div>
      <div class="item">Ginger Beer<span class="dots"></span>$3.95</div>
      <div class="item">Mount Alder Water<span class="dots"></span>$2.50</div>
      <div class="item">Rally Energy Drink (375 ml)<span class="dots"></span>$3.95</div>
    </div>
    <div class="dinner">
      <div class="item">DINNER PACK<span class="dots"></span>$25</div>
      <p class="pack"><b>Pizza Pack - </b>Cheesy Garlic Bread, Any Large Pizza (Excl<br>Premium range), Any Dessert or 1.25 lit</p>
      <p class="pack"><b>Pasta Pack - </b>Curly Fries, Any Pasta, Any Dessert or 1.25 lit</p>
      <p class="pack"><b>Parmi Pack - </b>Chips, Any Parmigiana, Any Dessert or 1.25 lit</p>
      <p class="pack"><b>Ribs &amp; Wings Pack - </b>Chips, Any Wings, Ribs (Pork or Beef)</p>
    </div>
  </section>

  <section class="panel deals-panel">
    <div class="photo deals-photo" role="img" aria-label="Photo of a sliced vegetable pizza with fresh tomatoes, capsicum and salad"></div>
    <div class="deals">
      <h2 class="heading">DEALS</h2>
      <p class="note">Free delivery $40 and Over</p>
      <div class="deal"><div class="item">Party Deal<span class="dots"></span>$54.95</div><p>3 Large Pizza or Pasta, 2 Garlic Bread &amp; 1.25 lit Drink</p></div>
      <div class="deal"><div class="item">Family Deal<span class="dots"></span>$39.95</div><p>2 Large Pizza or Pasta, 2 Garlic Bread, 1.25 lit drink</p></div>
      <div class="deal"><div class="item">Couple Deal<span class="dots"></span>$24.95</div><p>1 Family Pizza, 1 Garlic Bread, 1.25 lit Drink</p></div>
      <div class="deal"><div class="item">Single Deal<span class="dots"></span>$19.95</div><p>1 Large Pizza or Pasta, 1 Garlic Bread, 1 can drink</p></div>
      <div class="deal"><div class="item">Small Deal<span class="dots"></span>$14.95</div><p>1 Small Pizza, 1 Garlic Bread, 1 can drink - $14.95</p></div>
      <p class="terms">Terms &amp; Condition: (Large Pizza Excludes Premium &amp;<br>Seafood range,One&nbsp;&nbsp;Offer per order )</p>
    </div>
    <div class="contact">
      <p class="label">Contact Details</p>
      <p class="phone">CONTACT US : 07 3555 0142</p>
      <p class="addr">Brelvo Pizza &amp; Pasta<br>112 Harbour View Rd, Westbrook</p>
      <p class="web">LOG ON : www.brelvo.com.au</p>
    </div>
  </section>

  <section class="panel cover">
    <div class="brand-area">
      <span class="brand-mark"></span>
      <span class="brand-name">Brelvo Pizza &amp; Pasta</span>
    </div>
    <div class="photo pizza-photo" role="img" aria-label="Photo of a supreme pizza with olives, basil and rocket on a wooden board"></div>
    <div class="site-band">www.brelvo.com.au</div>
  </section>

</main>
</body>
</html>
```